Missing Traveler Patterns: Seizures

Book cover. Casebound and Perfect bound. Size 5.5 x 8.5 (portrait). Approx 165 pages for spine. Will be using Corvel PressWorks for printer so be sure to follow those specifications. This is a textbook for Search & Rescue and Law Enforcement search planners on deciding where they should look for someone who has been abducted. Nothing morbid. It will be a book in a series. The series is called Missing Traveler Patterns. That should be in smaller letters at the top. Seizures should be the major title feature. The series will have a border on the front cover of safety orange (255, 121, 0) for RGB. hvQ logo on front, spine, and back. Place holder for ISBN, author bio, book description, endorsements on back.

Target Market(s)

Professional textbook for Law Enforcement, Search and Rescue, Academic (criminologist)

Industry/Entity Type

Search and Rescue - Law Enforcement. Major colors for industry is orange for SAR and blue for Law enforcement

Requirements
Must have
• Safety Orange border (0.25 inch), hvQ Logos, small Missing Traveler Patterns title on top, large Seizures title. Author's name (Daniel P. Marwick)
Nice to have
• Not sure if picture or illustration works best. Topographic map is possible, law enforcement and searcher working together, clandestine grave, dirt road, all possible
Should not have
• no dead bodies, no bones, no skulls, no urban environment

```html
<!DOCTYPE html>
<html lang="en">
<head>
<meta charset="utf-8">
<title>Missing Traveler Patterns: Seizures — Cover</title>
<link href="https://fonts.googleapis.com/css2?family=Bebas+Neue&family=Poppins:wght@400;600&display=swap" rel="stylesheet">
<style>
  :root {
    --page-bg: #f6f6f6;
    --navy: #10307a;
    --navy-dark: #0b2566;
    --navy-title: #0f2e78;
    --band-orange: #f26c0c;
    --title-grey: #e6e6e8;
    --white: #ffffff;
  }
  * { box-sizing: border-box; margin: 0; padding: 0; }
  html, body {
    width: 1200px;
    height: 1140px;
    overflow: hidden;
    background: var(--page-bg);
  }
  .canvas {
    position: relative;
    width: 1200px;
    height: 1140px;
  }
  .book {
    position: absolute;
    left: 232px;
    top: 70px;
    width: 737px;
    height: 1000px;
    display: flex;
    box-shadow: 0 18px 40px rgba(0, 0, 0, 0.16);
  }

  /* Spine */
  .spine {
    position: relative;
    width: 90px;
    height: 100%;
    background: var(--navy-dark);
  }
  .spine-title {
    position: absolute;
    top: 70px;
    left: 50%;
    transform: translateX(-50%);
    writing-mode: vertical-rl;
    font-family: "Bebas Neue", sans-serif;
    font-size: 50px;
    line-height: 1;
    letter-spacing: 0.5px;
    color: var(--title-grey);
    white-space: nowrap;
  }
  .spine-title__accent { color: var(--band-orange); }
  .spine-mark {
    position: absolute;
    bottom: 70px;
    left: 50%;
    transform: translateX(-50%);
    writing-mode: vertical-rl;
    display: flex;
    align-items: center;
    gap: 8px;
  }
  .spine-mark__square {
    width: 16px;
    height: 16px;
    background: var(--white);
  }
  .spine-mark__name {
    font-family: "Poppins", sans-serif;
    font-weight: 600;
    font-size: 26px;
    line-height: 1;
    color: var(--white);
  }

  /* Front cover */
  .cover {
    position: relative;
    width: 647px;
    height: 100%;
    background: var(--navy);
    overflow: hidden;
  }
  .series-title {
    position: absolute;
    top: 78px;
    left: 0;
    width: 100%;
    text-align: center;
    font-family: "Bebas Neue", sans-serif;
    font-size: 64px;
    line-height: 1;
    color: var(--title-grey);
    letter-spacing: 0.5px;
  }
  .main-title {
    position: absolute;
    top: 142px;
    left: 0;
    width: 647px;
    height: 200px;
  }
  .main-title text {
    font-family: "Bebas Neue", sans-serif;
    font-size: 196px;
    letter-spacing: 3px;
  }
  .main-title__depth {
    fill: var(--band-orange);
    stroke: var(--band-orange);
    stroke-width: 22px;
    stroke-linejoin: round;
  }
  .main-title__face {
    fill: var(--navy-title);
    stroke: var(--band-orange);
    stroke-width: 14px;
    stroke-linejoin: round;
    paint-order: stroke fill;
  }
  .cover-art {
    position: absolute;
    top: 350px;
    left: 40px;
    width: 567px;
    height: 435px;
    background: radial-gradient(ellipse 60% 55% at 50% 40%,
      #f26c0c 0%, #e4680f 45%, rgba(16, 48, 122, 0) 100%);
  }
  .author-band {
    position: absolute;
    left: 0;
    bottom: 0;
    width: 100%;
    height: 215px;
    background: var(--band-orange);
  }
  .author-name {
    position: absolute;
    right: 40px;
    top: 56px;
    font-family: "Poppins", sans-serif;
    font-weight: 400;
    font-size: 24px;
    letter-spacing: 10px;
    color: var(--white);
    text-transform: uppercase;
    white-space: nowrap;
  }
  .publisher-mark {
    position: absolute;
    left: 40px;
    bottom: 48px;
    display: flex;
    align-items: center;
    gap: 10px;
  }
  .publisher-mark__square {
    width: 22px;
    height: 22px;
    background: var(--white);
  }
  .publisher-mark__name {
    font-family: "Poppins", sans-serif;
    font-weight: 600;
    font-size: 34px;
    line-height: 1;
    color: var(--white);
  }
</style>
</head>
<body>
<main class="canvas">
  <div class="book">
    <aside class="spine" aria-label="Spine">
      <p class="spine-title">Missing Traveler Patterns : <span class="spine-title__accent">Seizures</span></p>
      <div class="spine-mark">
        <span class="spine-mark__square"></span>
        <span class="spine-mark__name">hvQ</span>
      </div>
    </aside>

    <section class="cover" aria-label="Front cover">
      <p class="series-title">Missing Traveler Patterns</p>
      <svg class="main-title" viewBox="0 0 647 200" role="heading" aria-level="1" aria-label="Seizures">
        <text class="main-title__depth" x="317" y="186" text-anchor="middle">SEIZURES</text>
        <text class="main-title__face" x="324" y="178" text-anchor="middle">SEIZURES</text>
      </svg>

      <div class="cover-art" role="img" aria-label="Illustration area: a figure with bowed head beneath swirling orange thoughts"></div>

      <div class="author-band">
        <p class="author-name">Daniel P. Marwick</p>
        <div class="publisher-mark">
          <span class="publisher-mark__square"></span>
          <span class="publisher-mark__name">hvQ</span>
        </div>
      </div>
    </section>
  </div>
</main>
</body>
</html>
```